HVAC company business card design

We need a business card design for a HVAC company. The design must look professional. Both sides will be used. The total data to be on the business card is
Name
Position
Email
Direct Phone/Moile Phone
Company Contacts /Address, Phone, Fax, web)
All data will be submit once the design is confirmed. For generic purposes use;
Emre Toksoy
Managing Director
+902324815263 (Mobile)
4712 Sokak No: 9 KBSE Yenikent IZMIR TURKEY
Tel: +902324815263 Fax : +902324815269
www.luvon.com.tr

Target Market(s)

HVAC

Industry/Entity Type

Business

Contact Information for Business Card

The total data to be on the business card is
Name
Position
Email
Direct Phone/Moile Phone
Emre Toksoy
Managing Director
+902324815263 (Mobile)
www.luvon.com.tr
The BC will use both sides of the card. The front will include the full logo and the details for the business card holder. The business card can be divided into vertical/horizontal or to a special shape. The common data like the company address/phone/fax should be indicated elsewehere. The back can contain some part or the whole logo and must contain the web address.

Font styles to use
Serif
Sans Serif

Colors
0355a3
cfdfed

Requirements
Should not have
• Please be careful with the fonts, it shouldnt be too small or too big and must not interfere with the logo fonts. If you need to use a curvy shape please do not use as the logo is already curvy or use the curves from the logo (if it looks good, otherwise forget it)
• We are not in favor of pictograms, only if they are perfect use them.

```html
<!DOCTYPE html>
<html lang="en">
<head>
<meta charset="utf-8">
<title>Luvon Business Card</title>
<link href="https://fonts.googleapis.com/css2?family=Source+Sans+3:wght@400;600;700&display=swap" rel="stylesheet">
<style>
  :root {
    --stage: #2e2e2e;
    --paper: #ffffff;
    --brand-blue: #0355a3;
    --brand-light: #cfdfed;
    --tab-start: #5fb4ea;
    --tab-end: #1f6fc0;
    --back-start: #55bdf0;
    --back-end: #1f5fb0;
    --map-tone: rgba(20, 70, 150, 0.35);
    --navy: #1b3766;
    --ink: #3a3a3a;
    --link: #2a6fbf;
  }
  * { box-sizing: border-box; margin: 0; padding: 0; }
  html, body {
    width: 1200px; height: 716px; overflow: hidden;
    background: var(--stage);
    font-family: "Source Sans 3", Arial, sans-serif;
  }
  .canvas {
    position: relative; width: 1200px; height: 716px;
  }
  .card {
    position: absolute; top: 200px;
    width: 520px; height: 297px;
    border-radius: 2px;
    overflow: hidden;
  }
  .card-front { left: 60px; background: var(--paper); }
  .card-back {
    left: 620px;
    background: linear-gradient(135deg, var(--back-start), var(--back-end));
  }

  /* front */
  .name-tab { position: absolute; left: 0; top: 30px; width: 215px; height: 66px; }
  .name-tab svg { position: absolute; inset: 0; }
  .holder-name {
    position: absolute; left: 16px; top: 6px;
    color: #fff; font-weight: 700; font-size: 17px;
  }
  .holder-role {
    position: absolute; left: 16px; top: 28px;
    color: #fff; font-size: 12px;
  }
  .address {
    position: absolute; left: 16px; top: 118px;
    font-size: 12px; line-height: 16px; color: var(--ink);
  }
  .contacts {
    position: absolute; left: 225px; top: 192px;
    font-size: 12px; line-height: 17px; color: var(--ink);
  }
  .contacts b { color: var(--brand-blue); font-weight: 700; }
  .contacts .web { color: var(--link); }
  .logo {
    position: absolute; display: flex; align-items: center; gap: 10px;
  }
  .logo-dot {
    width: 38px; height: 38px; border-radius: 50%;
    background: var(--brand-blue);
  }
  .logo-name {
    font-weight: 700; font-size: 44px; letter-spacing: 2px;
    color: var(--navy); line-height: 1;
  }
  .card-front .logo { right: 30px; top: 30px; }

  /* back */
  .world-map {
    position: absolute; left: 60px; top: 20px; width: 400px; height: 220px;
    border-radius: 30px;
    background: radial-gradient(ellipse at center, var(--map-tone), rgba(20,70,150,0) 70%);
  }
  .card-back .logo { left: 50%; top: 112px; transform: translateX(-50%); }
  .card-back .logo-name { font-size: 56px; }
  .card-back .logo-dot { width: 48px; height: 48px; background: var(--brand-light); }
  .back-web {
    position: absolute; left: 0; right: 0; top: 222px;
    text-align: center; color: #fff; font-size: 15px; font-weight: 600;
  }
</style>
</head>
<body>
<div class="canvas">

  <section class="card card-front">
    <div class="name-tab">
      <svg width="215" height="66" viewBox="0 0 215 66">
        <defs>
          <linearGradient id="tabFill" x1="0" x2="1" y1="0" y2="0">
            <stop offset="0" stop-color="var(--tab-start)"/>
            <stop offset="1" stop-color="var(--tab-end)"/>
          </linearGradient>
        </defs>
        <path d="M0 0 H215 V50 H28 L14 66 V50 H0 Z" fill="url(#tabFill)"/>
      </svg>
      <div class="holder-name">Emre Toksoy</div>
      <div class="holder-role">Managing Director</div>
    </div>

    <div class="address">
      4712 Sokak No: 9<br>
      KBSE Yenikent IZMIR TURKEY
    </div>

    <div class="contacts">
      <b>P:</b> +902324815263<br>
      <b>F:</b> +902324815269<br>
      <span class="web">www.luvon.com.tr</span> | <b>E:</b> info@luvon.com
    </div>

    <div class="logo">
      <span class="logo-dot"></span>
      <span class="logo-name">LUVON</span>
    </div>
  </section>

  <section class="card card-back">
    <div class="world-map" role="img" aria-label="Dotted world map in darker blue"></div>
    <div class="logo">
      <span class="logo-dot"></span>
      <span class="logo-name">LUVON</span>
    </div>
    <div class="back-web">www.luvon.com.tr</div>
  </section>

</div>
</body>
</html>
```